Geschäftspapiere für eine Zahnarztpraxis
Zielgruppe
Zahnarztpraxis
Aufgabenstellung
Ich wünsche mir wenige grafische Elemente auf der Vorderseite. Die Rückseite soll komplett mit einer Grafik gefüllt sein.
Die Datei die ich als Fototapete zur Verfügung stelle, muss nicht zwangsläufig in dem Designvorschlag enthalten sein. Die Tapeten machen einen Großteil der Inneneinrichtung meiner Praxis aus. Sie sind ein Wiedererkennungsmerkmal, daher dachte ich, es würde Sinn ergeben, diese zum Teil in das Design einfließen zu lassen.

```html
<!DOCTYPE html>
<html lang="de">
<head>
<meta charset="utf-8">
<title>Briefbogen – Zahnarztpraxis Lindqvist &amp; Team</title>
<link href="https://fonts.googleapis.com/css2?family=Open+Sans:wght@400;700&family=Montserrat:wght@400&display=swap" rel="stylesheet">
<style>
  :root {
    --backdrop: #e4e5e3;
    --paper: #ffffff;
    --brand-green: #3f7467;
    --footer-band: #8fb0aa;
    --footer-text: #eef4f2;
    --ink: #3d3d3d;
    --floral-a: #cfe6e4;
    --floral-b: #f3c9d4;
    --floral-c: #f6d9c4;
    --floral-d: #d8cde6;
    --floral-e: #e9f1ee;
  }
  * { margin: 0; padding: 0; box-sizing: border-box; }
  html, body { width: 1200px; height: 1200px; overflow: hidden; background: var(--backdrop); }

  .reverse-side {
    position: absolute; left: 206px; top: 159px; width: 656px; height: 938px;
    box-shadow: 0 6px 24px rgba(0,0,0,.14);
    background: linear-gradient(180deg, var(--floral-e) 0%, var(--floral-a) 14%, var(--floral-b) 28%, var(--floral-e) 40%, var(--floral-d) 52%, var(--floral-a) 64%, var(--floral-c) 78%, var(--floral-b) 90%, var(--floral-e) 100%);
  }
  .reverse-seam { position: absolute; left: 0; top: 569px; width: 100%; height: 2px; background: var(--paper); }

  .letterhead {
    position: absolute; left: 298px; top: 78px; width: 656px; height: 922px;
    background: var(--paper); box-shadow: 0 6px 24px rgba(0,0,0,.16);
    font-family: "Open Sans", sans-serif; color: var(--ink);
  }
  .wallpaper-strip {
    position: absolute; left: 547px; top: 0; width: 109px; height: 878px;
    background: linear-gradient(180deg, var(--floral-a) 0%, var(--floral-d) 22%, var(--floral-a) 45%, var(--floral-b) 62%, var(--floral-c) 80%, var(--floral-b) 100%);
  }
  .wallpaper-notch { position: absolute; left: 547px; top: 37px; width: 17px; height: 155px; background: var(--paper); }
  .wallpaper-seam { position: absolute; left: 547px; top: 565px; width: 109px; height: 2px; background: var(--paper); }

  .brand {
    position: absolute; left: 262px; width: 240px; top: 66px; text-align: center;
    color: var(--brand-green); font-weight: 400;
  }
  .brand-mark { display: block; margin: 0 auto 8px; width: 52px; height: 52px; border: 1.3px solid var(--brand-green); border-radius: 50%; }
  .brand-line-small { font-size: 14.5px; letter-spacing: .4px; line-height: 18px; }
  .brand-line-large { font-size: 18.5px; letter-spacing: 1.1px; line-height: 22px; }

  .salutation { position: absolute; left: 176px; top: 250px; font-size: 25px; font-weight: 400; line-height: 32px; }
  .letter-body { position: absolute; left: 176px; top: 303px; width: 444px; font-size: 12.2px; line-height: 14.6px; }
  .letter-body p { margin-bottom: 14.6px; }
  .letter-body p.joined { margin-bottom: 0; }
  .closing { position: absolute; left: 176px; top: 688px; font-size: 13.5px; letter-spacing: 3.2px; line-height: 18px; }
  .signature-scribble { position: absolute; left: 398px; top: 743px; width: 201px; height: 20px; background: linear-gradient(90deg, rgba(60,60,60,0) 0%, rgba(60,60,60,.16) 50%, rgba(60,60,60,0) 100%); border-radius: 10px; }
  .signer { position: absolute; left: 420px; width: 160px; top: 776px; text-align: center; }
  .signer-name { font-size: 14.5px; font-weight: 700; letter-spacing: 3.6px; line-height: 18px; }
  .signer-role { font-size: 12.5px; line-height: 16px; margin-top: 4px; }

  .contact-band {
    position: absolute; left: 0; top: 878px; width: 656px; height: 44px; background: var(--footer-band);
    font-family: "Montserrat", sans-serif; color: var(--footer-text); font-size: 7px; letter-spacing: 1.1px;
  }
  .contact-item { position: absolute; top: 0; height: 44px; display: flex; align-items: center; gap: 7px; line-height: 8px; }
  .contact-item svg { width: 8px; height: 8px; fill: var(--brand-green); flex: none; }
</style>
</head>
<body>
<section class="reverse-side" role="img" aria-label="Back of the letterhead, fully covered with the pastel floral wallpaper motif in mint, pink, peach and lilac">
  <div class="reverse-seam"></div>
</section>

<main class="letterhead">
  <div class="wallpaper-strip" role="img" aria-label="Soft pastel floral wallpaper motif in mint, pink, peach and lilac"></div>
  <div class="wallpaper-notch"></div>
  <div class="wallpaper-seam"></div>

  <header class="brand">
    <span class="brand-mark"></span>
    <div class="brand-line-small">ZAHNARZTPRAXIS</div>
    <div class="brand-line-large">LINDQVIST &amp; TEAM</div>
  </header>

  <h1 class="salutation">Dear Matthis,</h1>

  <section class="letter-body">
    <p>Lorem ipsum dolor sit amet, consectetuer adipiscing elit, sed diam nonummy nibh euismod tincidunt ut laoreet dolore magna aliquam erat volutpat. Ut wisi enim ad minim veniam, quis nostrud exerci tation ullamcorper suscipit lobortis nisl ut aliquip ex ea commodo consequat. Duis autem vel eum iriure dolor in hendrerit in vulputate velit esse molestie consequat, vel illum dolore eu feugiat nulla facilisis at vero eros et accumsan et iusto odio dignissim qui blandit praesent luptatum zzril delenit augue duis dolore te feugait nulla facilisi.</p>
    <p class="joined">Lorem ipsum dolor sit amet, cons ectetuer adipiscing elit, sed diam nonummy nibh euismod tincidunt ut laoreet dolore magna aliquam erat volutpat. Ut wisi enim ad minim veniam, quis nostrud exerci tation ullamcorper suscipit lobortis nisl ut aliquip ex ea commodo consequat.</p>
    <p>Lorem ipsum dolor sit amet, consectetuer adipiscing elit, sed diam nonummy nibh euismod tincidunt ut laoreet dolore magna aliquam erat volutpat. Ut wisi enim ad minim veniam, quis nostrud exerci tation ullamcorper suscipit lobortis nisl ut aliquip ex ea commodo consequat. Duis autem vel eum iriure dolor in hendrerit in vulputate velit esse molestie consequat, vel illum dolore eu feugiat nulla facilisis at vero eros et accumsan et iusto odio dignissim qui blandit praesent luptatum zzril delenit augue duis dolore te feugait nulla facilisi.</p>
    <p>Lorem ipsum dolor sit amet, cons ectetuer adipiscing elit, sed diam nonummy nibh euismod tincidunt ut laoreet dolore magna aliquam erat volutpat.</p>
  </section>

  <p class="closing">Sincerely, penkoru.</p>

  <div class="signature-scribble" role="img" aria-label="Handwritten signature"></div>
  <div class="signer">
    <div class="signer-name">penkoru</div>
    <div class="signer-role">Manager</div>
  </div>

  <footer class="contact-band">
    <div class="contact-item" style="left:89px">
      <svg viewBox="0 0 24 24"><path d="M6.6 10.8a15 15 0 0 0 6.6 6.6l2.2-2.2a1 1 0 0 1 1-.25 11.4 11.4 0 0 0 3.6.57 1 1 0 0 1 1 1V20a1 1 0 0 1-1 1A17 17 0 0 1 3 4a1 1 0 0 1 1-1h3.5a1 1 0 0 1 1 1c0 1.25.2 2.45.57 3.57a1 1 0 0 1-.25 1z"/></svg>
      <span>+4915100238817</span>
    </div>
    <div class="contact-item" style="left:205px">
      <svg viewBox="0 0 24 24"><path d="M2 8c3-4 17-4 20 0l-2 3-4-1V8H8v2l-4 1zM6 12h12l2 8H4z"/></svg>
      <span>+4969400127735</span>
    </div>
    <div class="contact-item" style="left:318px">
      <svg viewBox="0 0 24 24"><path d="M12 2a7 7 0 0 0-7 7c0 5 7 13 7 13s7-8 7-13a7 7 0 0 0-7-7zm0 9.5A2.5 2.5 0 1 1 12 6.5a2.5 2.5 0 0 1 0 5z"/></svg>
      <span>Lindenhofweg 14<br>D-35410 Hungen</span>
    </div>
    <div class="contact-item" style="left:461px">
      <svg viewBox="0 0 24 24"><path d="M3 5h18v14H3zm2 2v.5l7 5 7-5V7z"/></svg>
      <span>kontakt@lindqvist-zahn.de</span>
    </div>
  </footer>
</main>
</body>
</html>
```